Business Cards and Stationery
Vellomar Development Company
I need single sided standard sized Business Card [3.5" x 2"]
Not sure. Use something compatible with logo.
Professional
Xxxx Xxxxxxx
President
12345 Xxxxxxxxx Xxxxx
Xxxxxxxxx, Xxxxxxxxxx 12345
xxxxxxxxxxx@xxxxxxxxx.xxx
Contractor's License No. 123456
Not that the information will serve as placeholders until the project is awarded and finalized. Actual information will be provided to create final source files.

```html
<!DOCTYPE html>
<html lang="en">
<head>
<meta charset="utf-8">
<title>Vellomar Development Company – Stationery</title>
<link rel="stylesheet" href="https://fonts.googleapis.com/css2?family=Roboto:wght@400;700&display=swap">
<style>
  :root {
    --navy-deep: #141c52;
    --navy: #24307a;
    --navy-light: #4656a8;
    --ink: #222633;
    --grey-text: #5a5f6e;
    --paper: #ffffff;
    --backdrop: #e6e7ea;
    --shadow: rgba(20, 24, 40, 0.18);
  }
  * { margin: 0; padding: 0; box-sizing: border-box; }
  html, body { width: 1200px; height: 686px; overflow: hidden; }
  body {
    background: var(--backdrop);
    font-family: "Roboto", Arial, sans-serif;
    color: var(--ink);
    position: relative;
  }
  .sheet {
    position: absolute;
    background: var(--paper);
    box-shadow: 0 2px 8px var(--shadow);
    overflow: hidden;
  }
  .band { position: absolute; left: 0; width: 100%; display: block; }

  .brand { position: absolute; display: flex; align-items: center; gap: 6px; }
  .brand-dot { border-radius: 50%; background: var(--navy); flex: none; }
  .brand-name { font-weight: 700; letter-spacing: 0.06em; color: var(--navy-deep); line-height: 1; }
  .brand--light .brand-dot { background: var(--paper); }
  .brand--light .brand-name { color: var(--paper); }

  .contact { position: absolute; font-size: 5.5px; line-height: 1.6; color: var(--grey-text); }
  .contact b { color: var(--ink); }
  .contact--light { color: #e4e7f5; }
  .contact--light b { color: var(--paper); }

  /* Letterheads */
  .letterhead { top: 108px; width: 333px; height: 425px; }
  .letterhead--plain { left: 432px; }
  .letterhead--banded { left: 764px; }

  /* Envelopes */
  .envelope-c { left: 283px; top: 283px; width: 322px; height: 221px; }
  .envelope-dl { left: 566px; top: 211px; width: 365px; height: 144px; z-index: 2; }

  /* Business cards */
  .card { left: 1003px; width: 173px; height: 99px; }
  .card--front { top: 212px; }
  .card--back { top: 322px; background: linear-gradient(135deg, var(--navy-light), var(--navy-deep)); }
  .card-person { position: absolute; left: 10px; top: 12px; }
  .card-person .name { font-size: 6.5px; font-weight: 700; color: var(--navy-deep); }
  .card-person .role { font-size: 5px; color: var(--grey-text); }
</style>
</head>
<body>

<!-- Letterhead, plain -->
<section class="sheet letterhead letterhead--plain" aria-label="Letterhead">
  <div class="brand" style="left:14px;top:14px;">
    <span class="brand-dot" style="width:18px;height:18px;"></span>
    <span class="brand-name" style="font-size:16px;">VELLOMAR</span>
  </div>
  <p class="contact" style="left:14px;top:42px;">
    12345 Xxxxxxxx Xxxxx, Xxxxxxxx, Xxxxxxxx 12345<br>
    <b>Phone:</b> (123) 456-7890 &nbsp; <b>Fax:</b> (123) 456-7891<br>
    <b>Email:</b> xxxxxxxx@xxxxxxxx.xxx
  </p>
</section>

<!-- Letterhead, with footer band -->
<section class="sheet letterhead letterhead--banded" aria-label="Letterhead with footer">
  <div class="brand" style="left:12px;top:12px;">
    <span class="brand-dot" style="width:18px;height:18px;"></span>
    <span class="brand-name" style="font-size:16px;">VELLOMAR</span>
  </div>
  <svg class="band" style="bottom:0;height:80px;" viewBox="0 0 333 80" preserveAspectRatio="none" aria-hidden="true">
    <defs>
      <linearGradient id="lhBand" x1="0" y1="0" x2="1" y2="1">
        <stop offset="0" stop-color="#4656a8"/><stop offset="1" stop-color="#141c52"/>
      </linearGradient>
    </defs>
    <path d="M0 30 Q170 58 333 8 L333 80 L0 80 Z" fill="url(#lhBand)"/>
    <path d="M0 22 Q170 50 333 0" fill="none" stroke="#1b1f2e" stroke-width="2"/>
    <path d="M0 27 Q170 55 333 5" fill="none" stroke="#ffffff" stroke-width="1.5"/>
  </svg>
  <p class="contact contact--light" style="left:12px;bottom:8px;">
    12345 Xxxxxxxx Xxxxx, Xxxxxxxx, Xxxxxxxx 12345<br>
    <b>Phone:</b> (123) 456-7890 &nbsp; <b>Fax:</b> (123) 456-7891 &nbsp; <b>Email:</b> xxxxxxxx@xxxxxxxx.xxx
  </p>
</section>

<!-- C envelope -->
<section class="sheet envelope-c" aria-label="Envelope">
  <div class="brand" style="left:32px;top:38px;">
    <span class="brand-dot" style="width:16px;height:16px;"></span>
    <span class="brand-name" style="font-size:15px;">VELLOMAR</span>
  </div>
  <svg class="band" style="bottom:0;height:66px;" viewBox="0 0 322 66" preserveAspectRatio="none" aria-hidden="true">
    <defs>
      <linearGradient id="envBand" x1="0" y1="0" x2="1" y2="1">
        <stop offset="0" stop-color="#4656a8"/><stop offset="1" stop-color="#141c52"/>
      </linearGradient>
    </defs>
    <path d="M0 22 Q160 4 322 18 L322 66 L0 66 Z" fill="url(#envBand)"/>
    <path d="M0 14 Q160 -4 322 10" fill="none" stroke="#1b1f2e" stroke-width="2"/>
    <path d="M0 19 Q160 1 322 15" fill="none" stroke="#ffffff" stroke-width="1.5"/>
  </svg>
  <p class="contact contact--light" style="left:10px;bottom:22px;">12345 Xxxxxxxx Xxxxx, Xxxxxxxx, Xxxxxxxx 12345</p>
</section>

<!-- DL envelope, flap open -->
<section class="sheet envelope-dl" aria-label="DL envelope">
  <svg class="band" style="top:0;height:46px;" viewBox="0 0 365 46" preserveAspectRatio="none" aria-hidden="true">
    <defs>
      <linearGradient id="flap" x1="0" y1="0" x2="1" y2="0">
        <stop offset="0" stop-color="#141c52"/><stop offset=".5" stop-color="#4656a8"/><stop offset="1" stop-color="#141c52"/>
      </linearGradient>
    </defs>
    <path d="M0 0 L365 0 L340 34 Q182 46 25 34 Z" fill="url(#flap)"/>
    <path d="M0 0 L25 34 Q182 46 340 34 L365 0" fill="none" stroke="#c9ccd6" stroke-width="1"/>
  </svg>
  <div class="brand brand--light" style="left:150px;top:9px;">
    <span class="brand-dot" style="width:11px;height:11px;"></span>
    <span class="brand-name" style="font-size:11px;">VELLOMAR</span>
  </div>
</section>

<!-- Business card, front -->
<section class="sheet card card--front" aria-label="Business card front">
  <div class="brand" style="right:8px;top:10px;">
    <span class="brand-dot" style="width:9px;height:9px;"></span>
    <span class="brand-name" style="font-size:9px;">VELLOMAR</span>
  </div>
  <div class="card-person">
    <p class="name">Xxxx Xxxxxxx</p>
    <p class="role">President</p>
  </div>
  <p class="contact" style="left:10px;top:40px;font-size:4.8px;">
    12345 Xxxxxxxxx Xxxxx<br>
    Xxxxxxxxx, Xxxxxxxxxx 12345<br>
    xxxxxxxxxxx@xxxxxxxxx.xxx<br>
    Contractor's License No. 123456
  </p>
  <svg class="band" style="bottom:0;height:12px;" viewBox="0 0 173 12" preserveAspectRatio="none" aria-hidden="true">
    <path d="M0 6 Q86 0 173 4 L173 12 L0 12 Z" fill="#24307a"/>
  </svg>
</section>

<!-- Business card, back -->
<section class="sheet card card--back" aria-label="Business card back">
  <div class="brand brand--light" style="left:32px;top:42px;">
    <span class="brand-dot" style="width:12px;height:12px;"></span>
    <span class="brand-name" style="font-size:13px;">VELLOMAR</span>
  </div>
</section>

</body>
</html>
```